Slider needed for Database Documentation Topic

We need a slider to promote a content area of a web site. I'm listing this as a poster because the posters I have seen on FrameHarbor portfolios most closely resemble the combination or art and text I am looking for.
The content area we are promoting with this graphic will clarify the design and use of a complicated database. The title of the content area is "The Kindled VQ Database" and the banner should use that title.
To 'illuminate' something means to cast light on it, and this content area will help shed light on a complicated thing – the content will use diagrams, text, and examples to clarify the database. Another meaning is that an illuminated manuscript is a manuscript brought to life with pictures, and in a way that is also what this content area will do.
One idea for the slider might be a light bulb, lamp, candle or flashlight lighting up the words "VQ Database". Another idea would be the type of illustration you see if you search for "Illuminated manuscript"
But I'm not committed to any particular idea - in the past I have been pleased to see ideas that are different than my own but accomplish the same thing, so please feel free to use your judgement or ask any questions.
In addition to the title (The Kindled VQ Database) the graphic should allow room for three smaller lines of text – the three bullet items below:
- Guide to understanding the VQ database
- Data sources, uses and relationships explained with illustrations
- New content! Customers
The last bullet item will change as the content is added.
Some particulars ...
SIZE - 600 high x 1200 wide pixels
PHOTOS vs ILLUSTRATION - I am open to either one.

```html
<!DOCTYPE html>
<html lang="en">
<head>
<meta charset="utf-8">
<title>The Kindled VQ Database</title>
<link rel="stylesheet" href="https://fonts.googleapis.com/css2?family=Anton&family=Questrial&display=swap">
<style>
  :root {
    --paper-light: #ffffff;
    --paper-mid: #ebebeb;
    --paper-edge: #d6d6d6;
    --ink: #111111;
    --ink-soft: #1c1c1c;
    --title-white: #ffffff;
    --line-white: #f2f2f2;
    --bulb-glow: #ffffff;
    --bulb-shade: #cfd1d3;
  }
  * { box-sizing: border-box; margin: 0; padding: 0; }
  html, body { width: 1200px; height: 600px; overflow: hidden; }
  body { background: var(--paper-light); }
  .slider {
    position: relative;
    width: 1200px;
    height: 600px;
    overflow: hidden;
    background: linear-gradient(115deg, var(--paper-edge) 0%, var(--paper-mid) 30%, var(--paper-light) 75%);
  }
  .shadow-block {
    position: absolute;
    inset: 0;
    width: 1200px;
    height: 600px;
  }
  .bulb {
    position: absolute;
    left: 1052px;
    top: 0;
    width: 96px;
    height: 190px;
    border-radius: 10px 10px 48px 48px;
    background: radial-gradient(ellipse at 45% 65%, var(--bulb-glow) 0%, #f3f4f5 45%, var(--bulb-shade) 100%);
  }
  .title {
    position: absolute;
    left: 140px;
    top: 14px;
    font-family: "Anton", "Oswald", sans-serif;
    font-weight: 400;
    font-size: 138px;
    line-height: 124px;
    letter-spacing: 4px;
    color: var(--title-white);
    text-transform: uppercase;
  }
  .title span { display: block; }
  .bullets {
    position: absolute;
    left: 137px;
    top: 456px;
    list-style: none;
    font-family: "Questrial", "Helvetica Neue", sans-serif;
    font-size: 22px;
    line-height: 32px;
    color: var(--line-white);
  }
</style>
</head>
<body>
  <main class="slider">
    <svg class="shadow-block" viewBox="0 0 1200 600" aria-hidden="true">
      <polygon fill="var(--ink)" points="0,222 152,40 335,40 335,150 858,150 872,178 858,280 850,290 850,402 892,452 884,518 800,600 0,600"/>
    </svg>
    <div class="bulb" role="img" aria-label="Photograph of a glowing spiral energy-saving light bulb hanging from above"></div>
    <h1 class="title">
      <span>The</span>
      <span>Kindled</span>
      <span>VQ Database</span>
    </h1>
    <ul class="bullets">
      <li>Guide to understanding the VQ database</li>
      <li>Data sources, uses and relationships explained with&nbsp; illustrations</li>
      <li>New content! Customers</li>
    </ul>
  </main>
</body>
</html>
```